OKRUVI card Technical Architecture

Hello everyone OKRUVI: It is a consulting firm in Architecture and Construction. I require a card duplexing, sober, elegant, classic but not boring. Update 1: Use the following data for the card. Name: Rodrigo Salcedo Mauricio Quintana Position: COO Twitter: @okruviTB Homepage: okruvi.net home address not include the participation of all thank you.

Target Market(s)

Construction companies, Architects and Consulting Engineers

Industry/Entity Type

Consulting

Contact Information for Business Card

Los campos que debe tener:
Nombre, Cargo, email, homepage y twitter

Font styles to use
Serif
Sans Serif
Other font styles liked:
• Me gustan playfair display, open sans y roboto, pero estoy sujeto a sus propuestas

Requirements
Must have
• Colors: Present combined proposals in white, red, gray and black Update 1: The two names must be clearly differentiated from the two surnames
Nice to have
• They are free to present their best proposals. I will bring them immediate feedback to the extent you can go see their designs. Complete data for card and logo files will give the winner the

```html
<!DOCTYPE html>
<html lang="es">
<head>
<meta charset="UTF-8">
<title>OKRUVI – Tarjeta de presentación</title>
<link rel="stylesheet" href="https://fonts.googleapis.com/css2?family=Montserrat:wght@300;400;700&display=swap">
<style>
  :root {
    --bg: #e4e4e6;
    --card-black: #050505;
    --card-white: #ffffff;
    --brand-red: #b3222a;
    --deep-red: #7a1116;
    --text-white: #ffffff;
    --text-grey: #2b2b2b;
    --shadow: rgba(0,0,0,0.25);
  }
  * { margin: 0; padding: 0; box-sizing: border-box; }
  html, body {
    width: 1200px; height: 900px; overflow: hidden;
    background: var(--bg);
    font-family: "Montserrat", sans-serif;
  }
  .canvas { position: relative; width: 1200px; height: 900px; }

  .card {
    position: absolute;
    width: 640px; height: 366px;
    border-radius: 22px;
    box-shadow: 0 14px 30px var(--shadow);
    overflow: hidden;
  }

  /* Front */
  .card-front { left: 110px; top: 60px; background: var(--card-black); }
  .front-lockup {
    position: absolute; left: 0; right: 0; top: 108px;
    display: flex; flex-direction: column; align-items: center;
  }
  .wordmark-row { display: flex; align-items: center; gap: 18px; }
  .wordmark-dot { width: 26px; height: 26px; border-radius: 50%; background: var(--brand-red); }
  .wordmark-front {
    color: var(--text-white); font-weight: 300;
    font-size: 58px; letter-spacing: 16px; line-height: 1;
  }
  .front-rule { width: 360px; height: 1px; background: var(--brand-red); margin-top: 10px; }
  .tagline {
    color: var(--brand-red); font-size: 17px; font-weight: 400;
    letter-spacing: 4.5px; margin-top: 6px;
  }
  .social {
    position: absolute; left: 0; right: 0; bottom: 62px;
    display: flex; justify-content: center; align-items: center; gap: 8px;
    color: var(--text-white); font-size: 14px;
  }
  .social-dot { width: 10px; height: 10px; border-radius: 50%; background: var(--brand-red); }

  /* Back */
  .card-back { left: 450px; top: 470px; background: var(--card-white); }
  .back-wordmark {
    position: absolute; right: 44px; top: 38px;
    color: var(--deep-red); font-weight: 700; font-size: 34px; letter-spacing: 4px;
  }
  .side-band {
    position: absolute; left: 0; bottom: 0;
    width: 24px; height: 170px;
    background: var(--deep-red);
    border-top-right-radius: 24px;
  }
  .contact-block { position: absolute; left: 48px; top: 150px; }
  .person-name {
    color: var(--deep-red); font-weight: 700; font-size: 24px; line-height: 1.05;
  }
  .person-role { color: var(--text-grey); font-size: 13px; margin: 2px 0 6px; }
  .contact-list { list-style: none; margin-top: 6px; }
  .contact-list li {
    display: flex; align-items: center; gap: 10px;
    color: var(--text-grey); font-size: 14px; line-height: 1.45;
  }
  .contact-list svg { width: 11px; height: 11px; fill: none; stroke: var(--deep-red); stroke-width: 1.6; }
</style>
</head>
<body>
<main class="canvas">

  <section class="card card-front" aria-label="Anverso de la tarjeta">
    <div class="front-lockup">
      <div class="wordmark-row">
        <span class="wordmark-dot"></span>
        <span class="wordmark-front">OKRUVI</span>
      </div>
      <div class="front-rule"></div>
      <div class="tagline">ARQUITECTURA TÉCNICA</div>
    </div>
    <div class="social">
      <span class="social-dot"></span>
      <span>@okruviTB</span>
    </div>
  </section>

  <section class="card card-back" aria-label="Reverso de la tarjeta">
    <div class="back-wordmark">OKRUVI</div>
    <div class="side-band"></div>
    <div class="contact-block">
      <p class="person-name">Rodrigo Salcedo</p>
      <p class="person-role">COO</p>
      <p class="person-name">Mauricio Quintana</p>
      <p class="person-role">Director de Operaciones</p>
      <ul class="contact-list">
        <li>
          <svg viewBox="0 0 12 12"><path d="M2 1.5 L4.5 1.5 L5.2 4 L3.8 5 Q5 7.5 7 8.2 L8 6.8 L10.5 7.5 L10.5 10 Q5 10.5 2 4 Z"/></svg>
          (+571) 999 999 9999
        </li>
        <li>
          <svg viewBox="0 0 12 12"><rect x="1" y="2.5" width="10" height="7"/><path d="M1 2.5 L6 6.5 L11 2.5"/></svg>
          info@@okruvi.net
        </li>
        <li>
          <svg viewBox="0 0 12 12"><circle cx="6" cy="6" r="4.8"/><ellipse cx="6" cy="6" rx="2" ry="4.8"/><path d="M1.2 6 H10.8"/></svg>
          www.okruvi.net
        </li>
      </ul>
    </div>
  </section>

</main>
</body>
</html>
```